Flyer für eine Benefizveranstaltung für den Brunnen Bau in Afrika! (A6)
Zielgruppe
Unser Verein hat sich spezialisiert auf die Errichtung von Wasserbrunnen in Afrika. Der Verein hat überwiegend Muslime als Mitglieder.
Aufgabenstellung
Es findet eine Benefizveranstaltung am 08.12.2013 statt. Diese Veranstaltung ist ein Bankett. Es soll ein Flyer werden A6 auf 2 Seiten, auf der einen Seite ist Emotion auf der anderen die Details zur Veranstaltung.
Vorne:
Vorne sollte unser Logo (oder Foto von unserer Arbeit?) sein. Oben nur eine Überschrift Quellenhilfe (als Logo) und die Überschrift: "S.O.S. Hilferuf - Bankett zur Rettung der Ummah" Und unten dann noch: "Bring jede Person die du kriegen kannst und alles Geld was du hast, es geht um Leben und Tod!"
Dann noch ein Hinweis: "Nur für Männer!"
Datum: 08.12.2013 - 12.00 - 20.00 Uhr
Umgebund Düsseldorf/Duisburg - Genauer Ort wird am Tage der Veranstaltung auf www.sozialnetz-beispiel.de/quellenhilfe bekannt gegeben.
Räumlichkeiten:
Professionelle Bild und Tontechnik
Beheizte Räumlichkeiten
XXL Mesjid Gebetsraum
Sicherheitsdienst auf dem gesamten Gelände
Inklusivleistungen:
Fester Sitzplatz für jeden Gast
Catering am Tisch
3 Gang Menu
Softdrinks
Cay & Coffee House
Candy Bar
Programm:
Prämiere: Vorstellung von Quellenhilfe "Der starke Kreis"
Blutsauger - Die total verrückte Auktion (Neuheit!)
Mini Expo - Schausteller Tribühne
Überraschungsgast
Preis: Karte: 25,00 € pro Person (Begrenzte Anzahl)
Fragen und Vorverkauf:
E-Mail Adresse
Und dann unten vielleicht 5 Kästchen mit Profilbildern durchgestrichen. Mit dem Text: Keine Prominenz! Dies ist keine Spaß Veranstaltung!

```html
<!DOCTYPE html>
<html lang="de">
<head>
<meta charset="utf-8">
<title>Quellenhilfe – Benefizbankett Flyer</title>
<link href="https://fonts.googleapis.com/css2?family=Bebas+Neue&family=Bitter:ital,wght@0,400;0,700;1,400&family=Kalam:wght@400&display=swap" rel="stylesheet">
<style>
  :root{
    --stage:#3a3a3a;
    --paper:#ffffff;
    --red:#b3202a;
    --red-dark:#9c1a22;
    --blue:#2f5fa6;
    --blue-text:#2d6fc0;
    --ink:#2a2a2a;
    --gold-light:#fbf1d8;
    --gold:#f0c878;
    --gold-deep:#d9953a;
    --earth:#9a6a3c;
    --sky-blue:#8fb8e6;
    --silhouette:#b9b9b9;
  }
  *{margin:0;padding:0;box-sizing:border-box}
  html,body{width:1200px;height:853px;overflow:hidden;background:var(--stage)}
  body{position:relative;font-family:"Bitter",Georgia,serif;color:var(--ink)}

  .flyer{position:absolute;top:50px;height:761px;background:var(--paper);overflow:hidden;box-shadow:0 4px 14px rgba(0,0,0,.45)}
  .flyer--details{left:40px;width:556px}
  .flyer--cover{left:620px;width:542px}

  /* details side */
  .venue-list{position:absolute;left:24px;top:20px;list-style:none}
  .venue-list li{font-size:18px;line-height:25px;padding-left:20px;position:relative}
  .venue-list li::before{content:"";position:absolute;left:0;top:8px;width:10px;height:10px;background:var(--red)}

  .inclusive{position:absolute;left:22px;top:134px;border-left:3px solid var(--sky-blue);padding-left:10px;height:176px}
  .inclusive h2{font-size:19px;font-weight:700;color:var(--blue-text);letter-spacing:.5px;line-height:26px}
  .inclusive ul{list-style:none;margin-top:2px}
  .inclusive li{font-size:17.5px;line-height:25.4px;color:var(--blue-text);padding-left:16px;position:relative}
  .inclusive li::before{content:"";position:absolute;left:0;top:9px;width:8px;height:8px;background:var(--blue)}

  .brand-mark{position:absolute;left:320px;top:150px;width:200px;height:156px;display:flex;flex-direction:column;align-items:center;justify-content:flex-end}
  .brand-mark .dot{width:14px;height:14px;border-radius:50%;background:var(--blue-text);margin-bottom:8px}
  .brand-name{font-family:"Bitter",Georgia,serif;font-weight:700;font-size:26px;color:var(--ink)}
  .brand-url{font-size:11px;color:var(--ink);margin-top:-2px}

  .program{position:absolute;left:0;top:310px;width:556px;height:216px;background:var(--blue)}
  .program__tab{position:absolute;left:2px;top:14px;width:174px;height:32px;background:var(--red);color:#fff;font-weight:700;font-size:20px;letter-spacing:.5px;padding-left:20px;line-height:32px}
  .program ul{position:absolute;left:50px;top:56px;list-style:none;color:#fff}
  .program li{font-size:18px;line-height:21px;padding-left:18px;position:relative;margin-bottom:10px}
  .program li::before{content:"";position:absolute;left:0;top:6px;width:9px;height:9px;background:#fff}
  .program b{font-weight:700}

  .ticket-area{position:absolute;left:0;top:526px;width:556px;height:235px;background:linear-gradient(180deg,var(--gold-light) 0%,var(--gold) 55%,var(--gold-deep) 100%)}
  .price-bar{position:absolute;left:50px;top:10px;width:486px;height:34px;background:var(--red);color:#fff;font-size:16px;line-height:34px;padding-left:34px}
  .price-bar b{font-weight:700}
  .contact{position:absolute;left:48px;top:60px;font-size:15.5px;line-height:21px}
  .contact .row{display:flex}
  .contact .label{width:120px;letter-spacing:.5px}
  .contact b{font-weight:700}

  .no-celebs{position:absolute;left:48px;top:112px;width:486px;height:108px}
  .portrait{position:absolute;top:0;width:104px;height:108px;background:#f4f4f4}
  .portrait .silhouette{position:absolute;left:10px;top:6px;width:84px;height:102px;background:var(--silhouette)}
  .portrait svg{position:absolute;left:0;top:0}
  .no-celebs__note{position:absolute;left:-6px;top:16px;width:500px;font-family:"Kalam",cursive;font-size:31px;line-height:38px;color:var(--ink);transform:rotate(-3deg)}

  /* cover side */
  .cover-backdrop{position:absolute;inset:0;background:radial-gradient(ellipse at 50% 55%,#fffdf6 0%,var(--gold-light) 35%,var(--gold) 70%,var(--gold-deep) 100%)}
  .cracked-ground{position:absolute;left:0;top:620px;width:542px;height:141px;background:linear-gradient(180deg,#c79a62 0%,var(--earth) 100%)}
  .cover-title{position:absolute;left:0;top:36px;width:542px;text-align:center;font-family:"Bebas Neue",Impact,sans-serif;font-weight:400;font-size:72px;line-height:57px;color:var(--red-dark);white-space:nowrap}
  .cover-call{position:absolute;left:0;top:226px;width:542px;text-align:center;font-size:21px;line-height:28px;color:var(--ink)}
  .cover-brand{position:absolute;left:0;top:470px;width:542px;display:flex;flex-direction:column;align-items:center}
  .cover-brand .dot{width:16px;height:16px;border-radius:50%;background:var(--blue-text);margin-bottom:10px}
  .cover-brand .brand-name{font-size:30px}
  .cover-brand .brand-url{font-size:12px}
  .men-only{position:absolute;left:0;top:557px;width:542px;text-align:center;color:var(--red);font-size:20px}
  .date-bar{position:absolute;left:72px;top:588px;width:408px;height:36px;background:var(--red);color:#fff;text-align:center;font-size:23px;line-height:36px;letter-spacing:.5px}
</style>
</head>
<body>

<section class="flyer flyer--details">
  <ul class="venue-list">
    <li>Professionelle Bild und Tontechnik</li>
    <li>Beheizte Räumlichkeiten</li>
    <li>XXL Mesjid Gebetsraum</li>
    <li>Sicherheitsdienst auf dem gesamten Gelände</li>
  </ul>

  <div class="inclusive">
    <h2>INKLUSIVLEISTUNGEN:</h2>
    <ul>
      <li>Fester Sitzplatz für jeden Gast</li>
      <li>Catering am Tisch</li>
      <li>3 Gang Menu</li>
      <li>Softdrinks</li>
      <li>Cay &amp; Coffee House</li>
      <li>Candy Bar</li>
    </ul>
  </div>

  <div class="brand-mark">
    <span class="dot"></span>
    <span class="brand-name">Quellenhilfe</span>
    <span class="brand-url">www.quellenhilfe-beispiel.de</span>
  </div>

  <div class="program">
    <div class="program__tab">PROGRAMM:</div>
    <ul>
      <li><b>PRÄMIERE</b>:Vorstellung von<br>Quellenhilfe "Der starke Kreis"</li>
      <li>Blutsauger - Die total<br>verrückte Auktion (Neuheit!)</li>
      <li>Mini Expo - Schausteller Tribühne</li>
      <li>Überraschungsgast</li>
    </ul>
  </div>

  <div class="ticket-area">
    <div class="price-bar"><b>Preis: Karte: 25,00 € pro Person</b> <i>(Begrenzte Anzahl)</i></div>
    <div class="contact">
      <div class="row"><span class="label">FRAGEN UND</span><b>Yusuf Beispielmann: 0150 - 000 00 000</b></div>
      <div class="row"><span class="label">VORVERKAUF:</span><span>E-Mail: <b>info@quellenhilfe-beispiel.de</b></span></div>
    </div>

    <div class="no-celebs">
      <div class="portrait" style="left:0">
        <div class="silhouette" role="img" aria-label="Grauer Profilbild-Platzhalter"></div>
        <svg width="104" height="108"><line x1="14" y1="12" x2="92" y2="100" stroke="#b3202a" stroke-width="5"/><line x1="92" y1="12" x2="14" y2="100" stroke="#b3202a" stroke-width="5"/></svg>
      </div>
      <div class="portrait" style="left:126px">
        <div class="silhouette" role="img" aria-label="Grauer Profilbild-Platzhalter"></div>
        <svg width="104" height="108"><line x1="14" y1="12" x2="92" y2="100" stroke="#b3202a" stroke-width="5"/><line x1="92" y1="12" x2="14" y2="100" stroke="#b3202a" stroke-width="5"/></svg>
      </div>
      <div class="portrait" style="left:254px">
        <div class="silhouette" role="img" aria-label="Grauer Profilbild-Platzhalter"></div>
        <svg width="104" height="108"><line x1="14" y1="12" x2="92" y2="100" stroke="#b3202a" stroke-width="5"/><line x1="92" y1="12" x2="14" y2="100" stroke="#b3202a" stroke-width="5"/></svg>
      </div>
      <div class="portrait" style="left:382px">
        <div class="silhouette" role="img" aria-label="Grauer Profilbild-Platzhalter"></div>
        <svg width="104" height="108"><line x1="14" y1="12" x2="92" y2="100" stroke="#b3202a" stroke-width="5"/><line x1="92" y1="12" x2="14" y2="100" stroke="#b3202a" stroke-width="5"/></svg>
      </div>
      <p class="no-celebs__note">Keine Prominenz!<br>Dies ist keine Spaß Veranstaltung!</p>
    </div>
  </div>
</section>

<section class="flyer flyer--cover">
  <div class="cover-backdrop" role="img" aria-label="Helles Sonnenlicht über einer trockenen Landschaft"></div>
  <div class="cracked-ground" role="img" aria-label="Ausgetrockneter, rissiger Wüstenboden mit Wasserspritzern"></div>

  <h1 class="cover-title">S.O.S. Hilferuhilferuf<br>Bankett zur Rettung<br>der Ummah</h1>
  <p class="cover-call">Bring jede Person die du kriegen kannst<br>und alles Geld was du hast,<br>es geht um Leben und Tod!</p>

  <div class="cover-brand">
    <span class="dot"></span>
    <span class="brand-name">Quellenhilfe</span>
    <span class="brand-url">www.quellenhilfe-beispiel.de</span>
  </div>

  <p class="men-only">Nur für Männer!</p>
  <div class="date-bar">08.12.2013 &nbsp;|&nbsp; 12.00 - 20.00 Uhr</div>
</section>

</body>
</html>
```